"Tales of Quiet Harbors" Book Cover Design

I am seeking a dynamic, modern, and professional cover design for a book focused on groundbreaking science that explores how a supplement called plasmalogens can revitalize the brain, prevent Alzheimer’s, and safeguard memories. The design should strike a balance between being visually appealing and conveying the seriousness of the topic.

Target Market(s)

The target audience includes individuals who are curious about cutting-edge science and proactive approaches to brain health, as well as those seeking to better understand how to protect their cognitive functions and memories. The cover should resonate with readers interested in health, science, and self-improvement, while reflecting the book’s informative and empowering tone.

Requirements
Must have
• The quotation across the top of the page (this is a placeholder for now, it will be changed eventually) and the author's name.
Should not have
• You don't need to use the puzzle idea!

```html
<!DOCTYPE html>
<html lang="en">
<head>
<meta charset="utf-8">
<title>Tales of Quiet Harbors</title>
<link rel="stylesheet" href="https://fonts.googleapis.com/css2?family=Archivo+Black&family=Archivo:wght@400;700&display=swap">
<style>
  :root {
    --paper: #ffffff;
    --stone: #c8c8c8;
    --ink: #0a0a0a;
    --accent: #c01f2f;
    --sketch: #ececec;
  }
  * { margin: 0; padding: 0; box-sizing: border-box; }
  html, body { width: 927px; height: 1200px; overflow: hidden; background: var(--paper); }
  .cover {
    position: relative;
    width: 927px;
    height: 1200px;
    background: var(--stone);
    overflow: hidden;
    font-family: "Archivo", Arial, sans-serif;
    color: var(--ink);
  }
  .cover-frame {
    position: absolute;
    inset: 0;
    background: linear-gradient(135deg, #cfcfcf, #bdbdbd);
  }
  .cover-field {
    position: absolute;
    left: 118px;
    top: 112px;
    width: 752px;
    height: 1030px;
    background: var(--paper);
    border-radius: 60px 30px 70px 40px;
  }
  .tagline {
    position: absolute;
    top: 160px;
    left: 0;
    width: 100%;
    padding-left: 40px;
    text-align: center;
    font-size: 20.5px;
    line-height: 27px;
    letter-spacing: 0.2px;
    text-transform: uppercase;
  }
  .title-top {
    position: absolute;
    top: 290px;
    left: 0;
    width: 100%;
    padding-left: 40px;
    text-align: center;
    font-family: "Archivo Black", Arial, sans-serif;
    font-size: 76px;
    line-height: 1;
    letter-spacing: 1px;
  }
  .brain-art {
    position: absolute;
    left: 172px;
    top: 490px;
    width: 370px;
    height: 360px;
    background: radial-gradient(ellipse at 45% 45%, #f2f2f2, var(--sketch));
    border-radius: 48% 52% 44% 40% / 46% 48% 52% 54%;
  }
  .scatter {
    position: absolute;
    font-family: "Archivo Black", Arial, sans-serif;
    font-size: 98px;
    line-height: 1;
    color: var(--accent);
  }
  .scatter--q { left: 340px; top: 395px; transform: rotate(-4deg); }
  .scatter--u { left: 440px; top: 430px; transform: rotate(8deg); }
  .scatter--i { left: 545px; top: 545px; transform: rotate(-6deg); }
  .scatter--e { left: 560px; top: 700px; transform: rotate(12deg); }
  .scatter--t { left: 660px; top: 735px; transform: rotate(-14deg); }
  .title-bottom {
    position: absolute;
    left: 188px;
    top: 855px;
    width: 590px;
    height: 140px;
  }
  .title-bottom text {
    font-family: "Archivo Black", Arial, sans-serif;
    fill: var(--ink);
  }
  .author {
    position: absolute;
    top: 1024px;
    left: 0;
    width: 100%;
    padding-left: 40px;
    text-align: center;
    font-weight: 700;
    font-size: 21px;
    letter-spacing: 0.6px;
    text-transform: uppercase;
  }
</style>
</head>
<body>
  <main class="cover">
    <div class="cover-frame" role="img" aria-label="Grey cracked stone border framing the cover"></div>
    <div class="cover-field"></div>

    <p class="tagline">
      Explores how a supplement called<br>
      plasmalogens can revitalize the brain,<br>
      prevent Alzheimer’s, and safeguard memories.
    </p>

    <h1 class="title">
      <span class="title-top">Tales of</span>
      <span class="brain-art" role="img" aria-label="Black line drawing of a human brain breaking apart into fragments"></span>
      <span class="scatter scatter--q">Q</span>
      <span class="scatter scatter--u">U</span>
      <span class="scatter scatter--i">I</span>
      <span class="scatter scatter--e">E</span>
      <span class="scatter scatter--t">T</span>
      <svg class="title-bottom" viewBox="0 0 590 140" aria-label="Harbors">
        <text x="0" y="134" font-size="172" textLength="590" lengthAdjust="spacingAndGlyphs">HARBORS</text>
      </svg>
    </h1>

    <p class="author">By Daniel R Ashcroft, MD</p>
  </main>
</body>
</html>
```